Plakat-Design für Bauunternehmung
Zielgruppe
Wir sind eine Bauunternehmung (Meisterbetrieb und Ingenieurbüro) welche Erd- Maurer- und Betonarbeiten anbietet. Unser Fokus liegt auf Professionalität und qualitativ einwandfreie Arbeit. Wir sind teuer aber die besten in dem was wir machen. Unsere Zielgruppe liegt bei Kunden welche eine qualitativ einwandfreie Arbeit erwarten und bewusst sind dass das auch Geld kostet. Unserem Kunden ist die Geldfrage immer zweitrangig und er legt viel mehr wert auf andere Faktoren: Qualität, Zuverlässigkeit, Qualifikation, Termineinhaltung etc. Es ist selbstverständlich das die Kunden meist vermögender sind.
Aufgabenstellung
Format: 340 x 175 cm
Was muss drauf:
- Logo
- Firmendaten:
Lindmoosweg 7, 89079 Ulm
Telefon: +49 (0) 7305 - 4418273
Mobil: +49 (0) 176 - 20394857
E-Mail: mortek@beispielpost.de
- Zusätzliche Informationen: Es sollte irgendwo noch 'Bauunternehmung' stehen, es sollte etwas größer sein, unter Logo oder ähnlich, Es muss klar sein das wir eine Bauunternehmung sind. Zusätzlich dazu noch unsere Leistungen 'Neubau, Umbau, Anbau', nebeneinander oder übereinander ist euch überlassen.

```html
<!DOCTYPE html>
<html lang="de">
<head>
<meta charset="utf-8">
<title>mortek – Bauunternehmung Bauzaunbanner</title>
<link rel="stylesheet" href="https://fonts.googleapis.com/css2?family=Montserrat:wght@500;600;700&family=Source+Sans+3:wght@600&display=swap">
<style>
  :root {
    --page-bg: #dcdcdc;
    --banner-light: #f3f3f3;
    --band-dark: #2a2b2d;
    --band-dark-soft: #3b3c3f;
    --ink-on-dark: #f5f5f5;
    --ink-on-light: #2c2d2f;
  }
  html, body {
    margin: 0;
    padding: 0;
    width: 1200px;
    height: 864px;
    overflow: hidden;
    background: var(--page-bg);
  }
  .banner {
    position: absolute;
    left: 20px;
    top: 142px;
    width: 1160px;
    height: 580px;
    display: block;
  }
  .brand-name { font-family: "Montserrat", sans-serif; font-weight: 700; fill: var(--ink-on-light); }
  .brand-tagline { font-family: "Montserrat", sans-serif; font-weight: 500; fill: var(--ink-on-light); letter-spacing: 0.6px; }
  .headline { font-family: "Montserrat", sans-serif; font-weight: 700; fill: var(--ink-on-dark); }
  .services { font-family: "Montserrat", sans-serif; font-weight: 600; fill: var(--ink-on-dark); }
  .contact { font-family: "Source Sans 3", sans-serif; font-weight: 600; fill: var(--ink-on-dark); }
</style>
</head>
<body>
<svg class="banner" viewBox="0 0 1160 580" xmlns="http://www.w3.org/2000/svg" role="img" aria-label="Banner der mortek Bauunternehmung">
  <defs>
    <linearGradient id="band-fill" x1="0" y1="0" x2="1" y2="1">
      <stop offset="0" stop-color="var(--band-dark-soft)"/>
      <stop offset="1" stop-color="var(--band-dark)"/>
    </linearGradient>
  </defs>

  <rect class="banner-surface" x="0" y="0" width="1160" height="580" fill="var(--banner-light)"/>

  <g class="brand">
    <rect class="brand-square" x="283" y="42" width="146" height="146" fill="var(--ink-on-light)"/>
    <text class="brand-tagline" x="883" y="59" font-size="16" text-anchor="end">MEISTERBETRIEB &amp; INGENIEURBÜRO</text>
    <text class="brand-name" x="462" y="188" font-size="118" textLength="421" lengthAdjust="spacingAndGlyphs">mortek</text>
  </g>

  <path class="info-band" d="M0 266 L54 223 L1106 223 L1160 266 L1160 580 L0 580 Z" fill="url(#band-fill)"/>

  <text class="headline" x="580" y="317" font-size="78" text-anchor="middle">Bauunternehmung</text>
  <text class="services" x="580" y="392" font-size="56" text-anchor="middle">Neubau - Umbau - Anbau</text>

  <line class="band-rule" x1="76" y1="424" x2="1084" y2="424" stroke="var(--ink-on-dark)" stroke-width="2"/>

  <g class="contact-block">
    <text class="contact" x="336" y="481" font-size="30" text-anchor="middle">Lindmoosweg 7, 89079 Ulm</text>
    <text class="contact" x="336" y="536" font-size="30" text-anchor="middle">E-Mail: mortek@beispielpost.de</text>
    <line class="contact-divider" x1="580" y1="453" x2="580" y2="546" stroke="var(--ink-on-dark)" stroke-width="2"/>
    <text class="contact" x="615" y="481" font-size="30">Tel : +49 (0) 7305 - 4418273</text>
    <text class="contact" x="617" y="536" font-size="30">Mobil: +49 (0) 176 - 20394857</text>
  </g>
</svg>
</body>
</html>
```